Keldro Cybersecurity Secives professional web site

Keldro is a unit of the Vostemic company, based on the audit services it offers and which mainly works by the contacts it has from its previous experience. The objective with the development of this website will be to increase its presence on the internet and even link the traffic of its social networks with the blog of the new page and in this way, provide information for old and potential customers.
For this reason, we will set the objective of the page, have all the information of the company, its services and its scope in general, in a formal and simple for users, facilitating the task of finding the information they want within of the page, as well as, including the option of feedback.
Updates

Need extra days to review

Target Market(s)

any company that needs security assessments

Number of Pages Required

4 page

Font styles to use
Sans Serif

Colors

Designer to choose colors to be used in the design.

Requirements
Must have
• READ THE PDF PLEASE. Video in homepage, cool graphics, color like our logo
• I like the following sites: www.vostemic-example.com & www.gantrelo-example.com
Nice to have
• Futuristic
Should not have
• Please, dont use the gallery pictures I used in my document, I prefer hand made illustrations instead

```html
<!DOCTYPE html>
<html lang="en">
<head>
<meta charset="utf-8">
<title>Keldro Security</title>
<link href="https://fonts.googleapis.com/css2?family=Montserrat:wght@500;600;700;800&family=Roboto:wght@300;400;500;700&display=swap" rel="stylesheet">
<style>
  :root{
    --navy:#17273a;
    --navy-deep:#0b1e2d;
    --teal:#0f4a5c;
    --yellow:#f6c817;
    --red:#c8102e;
    --white:#ffffff;
    --ink:#1d2630;
    --grey:#8a8f96;
    --line:#e6e8eb;
    --heading:"Montserrat", Arial, sans-serif;
    --body:"Roboto", Arial, sans-serif;
  }
  *{box-sizing:border-box;margin:0;padding:0}
  html,body{width:1200px;height:2483px;overflow:hidden}
  body{background:var(--white);font-family:var(--body);color:var(--ink);position:relative}
  .wrap{position:relative;width:704px;margin-left:248px}

  /* Hero */
  .hero{position:relative;height:505px;overflow:hidden}
  .hero-art{position:absolute;inset:0;
    background:radial-gradient(circle at 800px 230px,#1f8fa6 0,#0f5a70 140px,#0b3347 300px,rgba(6,20,30,0) 520px),
               linear-gradient(90deg,#081824 0%,#0b2a3a 45%,#0c3446 70%,#06151f 100%);}
  .topbar{position:absolute;top:20px;left:248px;width:704px;height:40px;display:flex;align-items:center}
  .brand{display:flex;align-items:center;gap:10px;color:var(--white);font-family:var(--heading);font-weight:800;font-size:19px;line-height:19px;text-transform:uppercase}
  .brand-dot{width:58px;height:58px;border-radius:50%;background:var(--white)}
  .nav{margin-left:auto;display:flex;gap:20px;list-style:none;margin-right:30px}
  .nav a{color:var(--white);text-decoration:none;font-family:var(--heading);font-weight:600;font-size:12px}
  .lang{width:100px;height:32px;border-radius:16px;background:var(--red);color:var(--white);display:flex;align-items:center;justify-content:center;gap:6px;font-family:var(--heading);font-weight:600;font-size:10px}
  .lang-flag{width:14px;height:9px;background:#2a3b8f}
  .hero-copy{position:absolute;left:248px;top:168px;color:var(--white)}
  .hero-title{font-family:var(--heading);font-weight:800;font-size:41px;line-height:41px;text-transform:uppercase}
  .hero-title .accent{color:var(--yellow)}
  .hero-sub{margin-top:12px;font-family:var(--heading);font-weight:600;font-size:15px;line-height:21px;text-transform:uppercase}
  .btn-yellow{display:inline-flex;align-items:center;justify-content:center;margin-top:24px;width:142px;height:38px;border-radius:19px;background:var(--yellow);color:var(--ink);font-family:var(--heading);font-weight:700;font-size:11px;text-transform:uppercase}

  /* Sections */
  .section-title{font-family:var(--heading);font-weight:800;font-size:30px;color:var(--navy);text-align:center;text-transform:uppercase}
  .services{height:648px;padding-top:36px}
  .service-grid{display:grid;grid-template-columns:repeat(3,224px);column-gap:16px;row-gap:0;margin-top:32px}
  .service-img{height:197px;box-shadow:0 4px 10px rgba(0,0,0,.15)}
  .service-name{height:56px;padding-top:14px;font-family:var(--heading);font-weight:700;font-size:11.5px;line-height:14px;text-transform:uppercase;color:var(--ink)}

  .video-band{position:relative;height:337px;overflow:hidden;color:var(--white);text-align:center}
  .video-art{position:absolute;inset:0;background:linear-gradient(110deg,#1b2634 0%,#2b3848 45%,#3c4756 60%,#1d2835 100%)}
  .video-copy{position:relative;padding-top:102px}
  .video-title{font-family:var(--heading);font-weight:700;font-size:27px;text-transform:uppercase}
  .video-text{width:610px;margin:10px auto 0;font-size:10px;line-height:17px}
  .play{width:70px;height:70px;margin:18px auto 0;border-radius:50%;background:var(--white);display:flex;align-items:center;justify-content:center}

  .blogs{height:574px;padding-top:42px}
  .blog-grid{display:grid;grid-template-columns:repeat(3,224px);column-gap:16px;margin-top:32px}
  .blog-card{height:390px;background:var(--white);box-shadow:0 3px 12px rgba(0,0,0,.14)}
  .blog-img{height:221px}
  .blog-body{padding:18px 16px 0}
  .blog-date{font-size:10px;font-weight:500}
  .blog-title{margin-top:10px;font-family:var(--heading);font-weight:700;font-size:14.5px;line-height:17px;text-transform:uppercase}
  .blog-excerpt{margin-top:8px;font-size:9.5px;line-height:14px;color:var(--grey);font-weight:300}
  .blog-more{margin-top:10px;font-size:9.5px;font-weight:500;text-transform:uppercase}

  /* Footer */
  .footer{background:var(--navy);height:361px;color:var(--white);padding-top:60px}
  .footer-cols{display:flex}
  .footer-about{width:224px;padding-right:14px}
  .footer-brand{display:flex;align-items:center;gap:8px;font-family:var(--heading);font-weight:800;font-size:17px;line-height:17px;text-transform:uppercase}
  .footer-brand .brand-dot{width:42px;height:42px}
  .footer-about p{margin-top:18px;font-size:9.5px;line-height:16px;color:#d4d8dd}
  .socials{display:flex;gap:8px;margin-top:26px}
  .socials span{width:28px;height:28px;border-radius:50%;background:var(--white)}
  .footer-head{font-family:var(--heading);font-weight:700;font-size:12px;text-transform:uppercase}
  .footer-links{width:78px}
  .footer-links ul{list-style:none;margin-top:22px}
  .footer-links li{font-size:9.5px;line-height:25px;color:#d4d8dd}
  .footer-links li::before{content:"\203A";margin-right:6px}
  .footer-info{width:190px}
  .footer-info dl{margin-top:22px;font-size:9.5px;line-height:16px;color:#d4d8dd}
  .footer-info dt{display:inline;font-weight:700;color:var(--white)}
  .footer-info dd{display:inline}
  .footer-info .row{margin-bottom:10px}
  .footer-contact{width:211px}
  .field{margin-top:14px;height:40px;border:1px solid #6d7a89;border-radius:20px;padding:12px 18px;font-size:9px;color:#8d99a7}
  .field.message{margin-top:20px;height:83px;border-radius:18px}
  .send{margin-top:22px;width:115px;height:33px;border-radius:17px;background:var(--white);color:var(--ink);display:flex;align-items:center;justify-content:center;font-family:var(--heading);font-weight:700;font-size:10px}
  .footer-contact .field:first-of-type{margin-top:18px}
  .copyright{height:58px;background:var(--navy);border-top:1px solid #243549;color:#d4d8dd;font-size:9.5px;display:flex;align-items:center}
  .copyright b{color:var(--white)}
</style>
</head>
<body>

<header class="hero">
  <div class="hero-art" role="img" aria-label="Dark teal digital backdrop with a glowing shield and padlock emblem on circuitry"></div>
  <div class="topbar">
    <div class="brand"><span>Keldro<br>Security</span><span class="brand-dot"></span></div>
    <ul class="nav">
      <li><a href="#">Home</a></li>
      <li><a href="#">About</a></li>
      <li><a href="#">Services</a></li>
      <li><a href="#">Blog</a></li>
      <li><a href="#">Contact us</a></li>
    </ul>
    <div class="lang"><span class="lang-flag"></span>EN/SP
      <svg width="7" height="5" viewBox="0 0 7 5"><path d="M0 0h7L3.5 5z" fill="#fff"/></svg></div>
  </div>
  <div class="hero-copy">
    <h1 class="hero-title"><span class="accent">E</span>xperts in<br>Cybersecurity<br>Protect you<span class="accent">r</span></h1>
    <p class="hero-sub">Digital asset. We audit your company.<br>Excellent reputation</p>
    <a class="btn-yellow">Read more</a>
  </div>
</header>

<section class="services">
  <div class="wrap">
    <h2 class="section-title">Our Services</h2>
    <div class="service-grid">
      <div><div class="service-img" role="img" aria-label="Hand drawing bar charts on paper beside a coffee cup" style="background:linear-gradient(135deg,#c9a57c,#efeae2 50%,#a8835b)"></div><p class="service-name">External and internal audits</p></div>
      <div><div class="service-img" role="img" aria-label="Dark server room corridor" style="background:linear-gradient(180deg,#2a2d31,#5c6064 50%,#1c1e20)"></div><p class="service-name">Web page audits</p></div>
      <div><div class="service-img" role="img" aria-label="Tablet with wifi symbol and connected home devices" style="background:linear-gradient(135deg,#f4f6f9,#d7e6f6 50%,#3b7fd1)"></div><p class="service-name">Audits of phone and tablet<br>applications</p></div>
      <div><div class="service-img" role="img" aria-label="Hand holding a blue padlock circuit emblem" style="background:linear-gradient(135deg,#15202c,#1f48b8 55%,#2b3440)"></div><p class="service-name">Audits of IoT devices</p></div>
      <div><div class="service-img" role="img" aria-label="Light bulb filled with blue water" style="background:radial-gradient(circle at 50% 45%,#4d9fd6,#cfe3f0 45%,#fafafa 70%)"></div><p class="service-name">Source code audit</p></div>
      <div><div class="service-img" role="img" aria-label="Desk with laptop, papers and coffee seen from above" style="background:linear-gradient(135deg,#6d5844,#d9d4cb 50%,#4b3b2d)"></div><p class="service-name">Response to incidents</p></div>
    </div>
  </div>
</section>

<section class="video-band">
  <div class="video-art" role="img" aria-label="Hands typing on a laptop keyboard in dim blue light"></div>
  <div class="video-copy">
    <h2 class="video-title">Lorem ipsum is simply dummy text</h2>
    <p class="video-text">Lorem Ipsum is simply dummy text of the printing and typesetting industry. Lorem Ipsum has been the industry's standard dummy text ever since the 1500s, when an unknown printer took a galley of type and scrambled it to make a type specimen book</p>
    <div class="play"><svg width="24" height="28" viewBox="0 0 24 28"><path d="M2 1l21 13L2 27z" fill="#1d2630"/></svg></div>
  </div>
</section>

<section class="blogs">
  <div class="wrap">
    <h2 class="section-title">Blogs</h2>
    <div class="blog-grid">
      <article class="blog-card">
        <div class="blog-img" role="img" aria-label="Padlock resting on a laptop keyboard" style="background:linear-gradient(135deg,#9aa3ad,#2b3138 55%,#565e67)"></div>
        <div class="blog-body"><p class="blog-date">14 AUG 2018</p><h3 class="blog-title">Lorem ipsum is simply dummy text</h3><p class="blog-excerpt">Lorem Ipsum is simply dummy text of the printing and typesetting industry. Lorem Ipsum has been the industry's standard dummy text ever since the 1500s.</p><p class="blog-more">Read more</p></div>
      </article>
      <article class="blog-card">
        <div class="blog-img" role="img" aria-label="Hand touching a glowing blue padlock on a digital grid" style="background:linear-gradient(135deg,#0e2a4a,#2f73c4 50%,#0b1d33)"></div>
        <div class="blog-body"><p class="blog-date">14 AUG 2018</p><h3 class="blog-title">Lorem ipsum is simply dummy text</h3><p class="blog-excerpt">Lorem Ipsum is simply dummy text of the printing and typesetting industry. Lorem Ipsum has been the industry's standard dummy text ever since the 1500s.</p><p class="blog-more">Read more</p></div>
      </article>
      <article class="blog-card">
        <div class="blog-img" role="img" aria-label="Hand reaching toward a network of hexagon icons" style="background:linear-gradient(135deg,#6e5a5a,#b9b3b6 50%,#4f5b70)"></div>
        <div class="blog-body"><p class="blog-date">14 AUG 2018</p><h3 class="blog-title">Lorem ipsum is simply dummy text</h3><p class="blog-excerpt">Lorem Ipsum is simply dummy text of the printing and typesetting industry. Lorem Ipsum has been the industry's standard dummy text ever since the 1500s.</p><p class="blog-more">Read more</p></div>
      </article>
    </div>
  </div>
</section>

<footer>
  <div class="footer">
    <div class="wrap footer-cols">
      <div class="footer-about">
        <div class="footer-brand"><span>Keldro<br>Security</span><span class="brand-dot"></span></div>
        <p>Keldro provides security audits for firms of every size, known for clear reports and quick answers when an incident occurs. Started in Valmora and now based in Orsena, its small team of analysts works on network reviews, code checks and penetration testing.</p>
        <div class="socials"><span></span><span></span><span></span><span></span></div>
      </div>
      <div class="footer-links">
        <h4 class="footer-head">Link</h4>
        <ul><li>Home</li><li>About</li><li>Services</li><li>Blogs</li><li>Videos</li><li>Contact us</li></ul>
      </div>
      <div class="footer-info">
        <h4 class="footer-head">Information</h4>
        <dl>
          <div class="row"><dt>Address</dt> <dd>: Av. Calderina, 41207<br>Orsena</dd></div>
          <div class="row"><dt>Phone Number</dt> <dd>: +34 955 214 330</dd></div>
          <div class="row"><dt>hours</dt> <dd>: Mon-Fri 8:30-17:30, Sat 9:00-12:00</dd></div>
          <div class="row"><dt>Website</dt> <dd>: www.keldrosecurity-example.com</dd></div>
        </dl>
      </div>
      <div class="footer-contact">
        <h4 class="footer-head">Contact us</h4>
        <div class="field">Email</div>
        <div class="field message">Message</div>
        <div class="send">SEND</div>
      </div>
    </div>
  </div>
  <div class="copyright"><div class="wrap">Copyright © 2018 <b>Keldro Security</b>. All rights reserved.</div></div>
</footer>

</body>
</html>
```